Copper Ridge Golf Circle Chart

I would like some type of design that can then be used on our website, like a png. or .jpeg or vector format. We want a circle/flow chart that describes our golf coaching process and has our logo faded in the background. attached is a rough draft to give you a general idea..something I created in word document but would like a much better version and attached is our logo. Our colors are red, black, and grey. The design does not necessarily have to have all of the bullet points..

Target Market(s)

Golfers, junior high golfers, high school golfers, adult golfers

Font styles to use
Sans Serif

Colors
ec1f27
f04a50
f59296
fbd4d5
aaaaaa
cbcbcb
1b1b1b
474747

Requirements
Nice to have
• Our colors are red, black, and grey, do not have to use all 3 in one design. Also The design does not necessarily have to have all of the bullet points.

```html
<!DOCTYPE html>
<html lang="en">
<head>
<meta charset="utf-8">
<title>Copper Ridge Golf Circle Chart</title>
<link rel="stylesheet" href="https://fonts.googleapis.com/css2?family=Lato:wght@700;900&family=Roboto+Condensed:wght@400&display=swap">
<style>
  :root {
    --red: #ec1f27;
    --red-soft: #ec3c38;
    --red-mid: #e8231f;
    --red-deep: #c20e0f;
    --red-dark: #9e0808;
    --ink: #1b1b1b;
    --grey: #474747;
    --paper: #ffffff;
  }
  html, body {
    margin: 0;
    width: 989px;
    height: 1200px;
    overflow: hidden;
    background: var(--paper);
  }
  .chart {
    display: block;
    width: 951px;
    height: 1200px;
    margin: 0 auto;
  }
  .chart-title { font-family: "Lato", sans-serif; font-weight: 900; font-size: 46px; }
  .chart-title .brand { fill: var(--red); }
  .chart-title .subject { fill: var(--grey); }
  .step-label { font-family: "Lato", sans-serif; font-weight: 700; font-size: 31px; text-anchor: middle; }
  .step-label--top { fill: var(--red); }
  .step-label--dark { fill: var(--red-dark); }
  .wheel-label { font-family: "Lato", sans-serif; font-weight: 700; font-size: 31px; fill: #fff; text-anchor: middle; }
  .bullet-text { font-family: "Roboto Condensed", sans-serif; font-size: 23px; fill: var(--ink); }
  .brand-mark { font-family: "Lato", sans-serif; font-weight: 900; font-size: 17px; fill: var(--red); text-anchor: middle; }
  .leader { fill: none; stroke-width: 2.5; stroke-dasharray: 9 6; }
  .leader--light { stroke: var(--red); }
  .leader--dark { stroke: var(--red-dark); }
  .cycle-arrow { fill: none; stroke: #fff; stroke-width: 6; }
</style>
</head>
<body>
<svg class="chart" viewBox="0 0 1000 1262" xmlns="http://www.w3.org/2000/svg" aria-labelledby="chartTitle">
  <defs>
    <filter id="bubbleShadow" x="-30%" y="-30%" width="160%" height="160%">
      <feDropShadow dx="0" dy="4" stdDeviation="7" flood-color="#000" flood-opacity="0.22"/>
    </filter>
    <radialGradient id="bubbleFill" cx="50%" cy="40%" r="60%">
      <stop offset="0" stop-color="#ffffff"/>
      <stop offset="1" stop-color="#eeeeee"/>
    </radialGradient>
    <marker id="arrowHead" viewBox="0 0 10 10" refX="3" refY="5" markerWidth="5" markerHeight="5" orient="auto" markerUnits="strokeWidth">
      <path d="M0 0 L10 5 L0 10 Z" fill="#fff"/>
    </marker>
  </defs>

  <text id="chartTitle" class="chart-title" x="500" y="126" text-anchor="middle"><tspan class="brand">COPPER RIDGE GOLF</tspan><tspan class="subject" dx="26">CIRCLE CHART</tspan></text>

  <g class="step-ribbon">
    <path d="M61 334 A111 111 0 0 1 283 334" fill="none" stroke="var(--red-soft)" stroke-width="22"/>
    <path d="M281 334 A111 111 0 0 0 503 334" fill="none" stroke="var(--red-mid)" stroke-width="22"/>
    <path d="M501 334 A111 111 0 0 1 723 334" fill="none" stroke="var(--red-deep)" stroke-width="22"/>
    <path d="M721 334 A111 111 0 0 0 943 334" fill="none" stroke="var(--red-dark)" stroke-width="22"/>
    <g filter="url(#bubbleShadow)" fill="url(#bubbleFill)">
      <circle cx="172" cy="334" r="96"/>
      <circle cx="392" cy="334" r="96"/>
      <circle cx="612" cy="334" r="96"/>
      <circle cx="832" cy="334" r="96"/>
    </g>
    <text class="step-label step-label--top" x="172" y="346">Evalution</text>
    <text class="step-label step-label--top" x="392" y="346">Coaching</text>
    <text class="step-label step-label--dark" x="612" y="346">Practice</text>
    <text class="step-label step-label--dark" x="832" y="328">Measure</text>
    <text class="step-label step-label--dark" x="832" y="359">Progress</text>
  </g>

  <path class="leader leader--light" d="M56 521 V753 H247"/>
  <path class="leader leader--light" d="M941 521 V750 H720"/>
  <path class="leader leader--dark" d="M242 923 H59 V1129"/>
  <path class="leader leader--dark" d="M732 920 H944 V1149"/>

  <g class="bullets bullets--evaluation">
    <circle cx="81" cy="530" r="7" fill="var(--red)"/><text class="bullet-text" x="107" y="538">Video Swing Analysis</text>
    <circle cx="81" cy="574" r="7" fill="var(--red)"/><text class="bullet-text" x="107" y="582">Putting Report</text>
    <circle cx="81" cy="618" r="7" fill="var(--red)"/><text class="bullet-text" x="107" y="626">Develop a Plan</text>
  </g>
  <g class="bullets bullets--coaching">
    <circle cx="640" cy="529" r="7" fill="var(--red)"/><text class="bullet-text" x="663" y="537">Tour Quaity Technology</text>
    <circle cx="640" cy="573" r="7" fill="var(--red)"/><text class="bullet-text" x="663" y="581">Visualization &amp; Feedback</text>
    <circle cx="640" cy="617" r="7" fill="var(--red)"/><text class="bullet-text" x="663" y="625">Understand Incon sitencies</text>
  </g>
  <g class="bullets bullets--progress">
    <circle cx="81" cy="1095" r="7" fill="var(--red-dark)"/>
    <text class="bullet-text" x="107" y="1103">Track Progress</text>
    <text class="bullet-text" x="107" y="1134">with Data</text>
  </g>
  <g class="bullets bullets--practice">
    <circle cx="640" cy="1094" r="7" fill="var(--red)"/><text class="bullet-text" x="663" y="1102">24/7 Access to Practice</text>
    <circle cx="640" cy="1138" r="7" fill="var(--red)"/><text class="bullet-text" x="663" y="1146">Practice with a Purpose</text>
  </g>

  <g class="process-wheel">
    <path d="M487 856 V600 A256 256 0 0 0 231 856 Z" fill="var(--red-soft)"/>
    <path d="M487 856 H743 A256 256 0 0 0 487 600 Z" fill="var(--red-mid)"/>
    <path d="M487 856 V1112 A256 256 0 0 0 743 856 Z" fill="var(--red-deep)"/>
    <path d="M487 856 H231 A256 256 0 0 0 487 1112 Z" fill="var(--red-dark)"/>
    <rect x="482" y="596" width="10" height="520" fill="#fff"/>
    <rect x="227" y="851" width="520" height="10" fill="#fff"/>

    <path class="cycle-arrow" d="M355 699 A205 205 0 0 1 620 700" marker-end="url(#arrowHead)"/>
    <path class="cycle-arrow" d="M685 806 A205 205 0 0 1 683 916" marker-end="url(#arrowHead)"/>
    <path class="cycle-arrow" d="M632 1001 A205 205 0 0 1 392 1038" marker-end="url(#arrowHead)"/>
    <path class="cycle-arrow" d="M294 926 A205 205 0 0 1 286 815" marker-end="url(#arrowHead)"/>

    <circle cx="487" cy="856" r="88" fill="var(--red)"/>
    <circle cx="487" cy="856" r="70" fill="#fff"/>
    <text class="brand-mark" x="487" y="852">Copper Ridge</text>
    <text class="brand-mark" x="487" y="874">Golf</text>

    <text class="wheel-label" x="378" y="758">Evalution</text>
    <text class="wheel-label" x="610" y="758">Coaching</text>
    <text class="wheel-label" x="369" y="963">Measure</text>
    <text class="wheel-label" x="369" y="994">Progress</text>
    <text class="wheel-label" x="598" y="975">Practice</text>
  </g>
</svg>
</body>
</html>
```